Glimo Sentara Winter Season (crossing course in the snow

Our company will diversify its activity. It will propose a crossing course to be carried out in the snow. We want the flyer to reflect the “far north” winter spirit.
This activity is unique in Switzerland. The flyer must catch the visual of the 80% tourist clientele and send them the desire to try
Target Market(s)
The clientele will be for all is all from 16 years
Industry/Entity Type
Tourisme d'hiver
Font styles to use
Sans Serif
Colors
Designer to choose colors to be used in the design.
Requirements
Must have
- The logo "Glimo Sentara" and "Combe-Saurel Pays Roches-du-Vent" and the 4 partner logos on the back must appear but cannot be modified except for the size while keeping the proportions. All texts must be on the flyer but can be changed according to the designer's style. Photos can be adapted and we want an attractive design concept with creativity matching the description. The format of the flyer must respect the template of the 2 files
Nice to have
- The color palette reflects winter tones
Should not have
- We are not interested in receiving a copy of my 2 files with only a font change and 2 size

```html
<!DOCTYPE html>
<html lang="fr">
<head>
<meta charset="utf-8">
<title>Glimo Sentara – Flyer hiver</title>
<link href="https://fonts.googleapis.com/css2?family=Exo+2:ital,wght@1,800;1,900&family=Montserrat:wght@500;600;700;800&display=swap" rel="stylesheet">
<style>
  :root {
    --stage: #2b2b2b;
    --paper: #ffffff;
    --teal: #68aab0;
    --teal-light: #86bfc3;
    --teal-deep: #5b9aa1;
    --ink: #1c1c1c;
    --contact: #1f5a5e;
    --snow-1: #f3f5f7;
    --snow-2: #cfd6dc;
    --snow-3: #9aa3ab;
    --accent-green: #7cc242;
    --partner-red: #d0161e;
    --partner-yellow: #ffe000;
  }
  * { box-sizing: border-box; margin: 0; padding: 0; }
  html, body { width: 1200px; height: 900px; overflow: hidden; background: var(--stage); }
  body { position: relative; font-family: "Montserrat", sans-serif; }

  .flyer {
    position: absolute; left: 275px; top: 31px;
    width: 650px; height: 838px;
    background: var(--paper); border-radius: 8px; overflow: hidden;
  }
  .visual {
    position: absolute; left: 8px; top: 7px; width: 636px; height: 712px; overflow: hidden;
  }
  .visual__photo {
    position: absolute; inset: 0;
    background:
      radial-gradient(ellipse at 35% 45%, var(--snow-1) 0%, transparent 55%),
      radial-gradient(ellipse at 8% 15%, var(--snow-3) 0%, transparent 35%),
      radial-gradient(ellipse at 45% 5%, var(--snow-2) 0%, transparent 40%),
      linear-gradient(170deg, var(--snow-2) 0%, var(--snow-1) 45%, #e6eaee 100%);
  }
  .visual__hills { position: absolute; inset: 0; width: 100%; height: 100%; }

  .brand {
    position: absolute; right: 24px; top: 110px;
    display: flex; align-items: center; gap: 7px;
    font-weight: 700; font-size: 26px; color: var(--ink); letter-spacing: -0.3px;
  }
  .brand__dot { width: 12px; height: 12px; border-radius: 50%; background: var(--accent-green); }

  .headline {
    position: absolute; right: 40px; top: 370px; text-align: right;
    font-family: "Exo 2", sans-serif; font-style: italic; font-weight: 900;
    font-size: 31px; line-height: 31px; color: #fff; letter-spacing: 0.6px;
  }
  .tagline {
    position: absolute; right: 37px; top: 452px;
    font-weight: 800; font-size: 15.5px; color: #fff;
  }
  .intro {
    position: absolute; right: 42px; top: 482px; width: 580px; text-align: right;
    font-weight: 600; font-size: 14px; line-height: 17.5px; color: #fff;
  }
  .intro p + p { margin-top: 16px; }

  .pricing {
    position: absolute; right: 283px; top: 592px; text-align: right; color: #fff;
    font-weight: 800; font-size: 16.5px; line-height: 22px;
  }
  .pricing__extra { margin-top: 3px; }
  .pricing__note { margin-top: 8px; font-weight: 700; font-size: 9px; line-height: 11px; }

  .session {
    position: absolute; left: 389px; top: 580px; width: 220px; height: 111px;
    background: var(--paper);
    clip-path: polygon(0 6%, 8% 2%, 14% 8%, 26% 4%, 38% 9%, 50% 3%, 64% 8%, 78% 2%, 90% 6%, 100% 0, 100% 100%, 90% 95%, 78% 99%, 64% 92%, 50% 97%, 38% 90%, 24% 96%, 12% 91%, 0 95%);
    display: flex; flex-direction: column; align-items: center; justify-content: center;
  }
  .session__title { font-weight: 800; font-size: 22px; line-height: 26px; color: var(--ink); }
  .session__row { display: flex; align-items: flex-end; gap: 8px; margin-left: 36px; }
  .session__brand { font-weight: 700; font-size: 10px; color: var(--ink); padding-bottom: 4px; }

  .partners {
    position: absolute; left: 0; right: 0; top: 722px; text-align: center;
  }
  .partners__title { font-weight: 800; font-size: 15px; color: var(--ink); margin-left: -30px; }
  .partners__row {
    display: flex; align-items: center; justify-content: space-between;
    padding: 0 35px 0 32px; margin-top: 9px; height: 34px;
  }
  .partner { display: flex; align-items: center; gap: 6px; font-weight: 700; font-size: 15px; color: var(--ink); }
  .partner--stack { font-size: 12.5px; line-height: 14px; text-align: left; }
  .partner__square { width: 22px; height: 22px; background: var(--partner-red); }
  .partner__mark { width: 35px; height: 35px; background: var(--partner-yellow); }

  .contact {
    position: absolute; left: 31px; right: 42px; top: 793px;
    display: flex; justify-content: space-between;
    font-weight: 700; font-size: 23px; color: var(--contact);
  }
</style>
</head>
<body>
  <main class="flyer">
    <section class="visual">
      <div class="visual__photo" role="img" aria-label="Photo de deux véhicules électriques tout-terrain roulant sur une piste enneigée en forêt de sapins"></div>
      <svg class="visual__hills" viewBox="0 0 636 712" preserveAspectRatio="none" aria-hidden="true">
        <path d="M0 420 L90 395 L180 345 L260 320 L330 290 L400 262 L480 215 L560 170 L636 120 L636 712 L0 712 Z" fill="var(--teal-light)"/>
        <path d="M0 402 L70 385 L140 372 L195 345 L270 328 L335 305 L400 285 L490 238 L560 205 L636 172 L636 712 L0 712 Z" fill="var(--teal)"/>
        <path d="M0 410 L50 440 L80 458 L120 425 L60 395 Z" fill="var(--teal-deep)" opacity="0.6"/>
        <path d="M0 712 L0 703 L40 698 L90 704 L150 696 L220 702 L300 695 L380 701 L460 694 L540 700 L600 693 L636 697 L636 712 Z" fill="#ffffff"/>
      </svg>
      <div class="brand"><span class="brand__dot"></span>Glimo Sentara</div>
    </section>

    <h1 class="headline">OUVERT TOUS LES JOURS<br>* DÈS 11H00</h1>
    <p class="tagline">UN CIRCUIT DE FRANCHISSEMENT SUR NEIGE.</p>
    <div class="intro">
      <p>Glimo Sentara vous propose une activité unique et inédite en Suisse.</p>
      <p>Avec nos Trackline®, nommées araignées électriques, arontez les<br>éléments mis en place sur nos parcours pour devenir le pilote tout<br>terrain que vous n’avez jamais imaginé être.</p>
    </div>

    <div class="pricing">
      <p>Indviduelle : CHF 40.</p>
      <p>Famille (4 personnes) : CHF140.</p>
      <p class="pricing__extra">SNACK - BAR - AMBIANCE&nbsp;</p>
      <p class="pricing__note">(*) : SOUS RÉSERVE DES CONDITIONS MÉTÉOROLOGIQUES</p>
    </div>

    <div class="session">
      <p class="session__title">SÉANCE DE</p>
      <div class="session__row">
        <p class="session__title">20MN</p>
        <span class="session__brand">Glimo Sentara</span>
      </div>
    </div>

    <section class="partners">
      <p class="partners__title">NOS PARTENAIRES :</p>
      <div class="partners__row">
        <span class="partner">Norvalis</span>
        <span class="partner">Fiduciaire Brémont S.A</span>
        <span class="partner partner--stack"><span class="partner__square"></span><span>Banque Alpine<br>du Sentier</span></span>
        <span class="partner"><span class="partner__mark"></span>KORVA</span>
      </div>
    </section>

    <footer class="contact">
      <span>info@glimo-sentara.ch</span>
      <span>I</span>
      <span>+41 77 000 12 34</span>
    </footer>
  </main>
</body>
</html>
```